General Contractor/ Real Estate Family Business AMAZING Drywall/Paint Flyer

We need to have a flyer designed to market our drywall repair services. We are looking to increase our business in this field and plan on using this flyer in both print and as an eflyer to use in email marketing campaigns. We would like to incorporate past flyer designs and colors/ logos into this flyer so our marketing stays consistent.

Target Market(s)

Drywall repair, Insurance Restoration, Real Estate Agents, Property Managers, Real Estate Investors, Single family residential homeowners.

Industry/Entity Type

Real Estate

Font styles to use
Sans Serif

Requirements
Must have
• Must include the logos provided, pictures provided, and incorporate the copy provided in the attached word document. Must include our license number. Must be able to fit a standard 8.5"x11" flyer size. Must also be optimized to use online as an eflyer in online marketing campaigns.
Nice to have
• It would be nice to incorporate some of the designs and colors form previous flyers to keep our marketing consistent. Past flyers are attached in the documents.

```html
<!DOCTYPE html>
<html lang="en">
<head>
<meta charset="UTF-8">
<title>Corvane Property Solutions – Drywall &amp; Painting Flyer</title>
<link rel="stylesheet" href="https://fonts.googleapis.com/css2?family=Barlow+Semi+Condensed:wght@400;500;600;700&family=Barlow+Condensed:wght@600;700&display=swap">
<style>
  :root {
    --ink: #141414;
    --white: #ffffff;
    --sky: #7fc4ec;
    --brand-blue: #1f4fa0;
    --bullet: #8fd0f5;
    --photo-sky: #5b93d8;
    --photo-tan: #b08a63;
    --photo-dark: #2c3646;
    --photo-dark-low: #3d3a34;
  }
  * { margin: 0; padding: 0; box-sizing: border-box; }
  html, body { width: 849px; height: 1200px; overflow: hidden; background: var(--ink); }
  body { font-family: "Barlow Semi Condensed", "Arial Narrow", sans-serif; color: var(--white); }
  .flyer { position: relative; width: 849px; height: 1200px; background: var(--ink); overflow: hidden; }

  /* Header */
  .header { position: absolute; left: 0; top: 0; width: 849px; height: 217px; background: var(--ink); }
  .brand { position: absolute; left: 52px; top: 98px; display: flex; align-items: center; gap: 12px; }
  .brand-mark { width: 18px; height: 18px; border-radius: 50%; background: var(--sky); }
  .brand-name { font-family: "Barlow Semi Condensed", sans-serif; font-weight: 600; font-size: 25px; color: var(--white); letter-spacing: 0.5px; }
  .license { position: absolute; left: 480px; top: 44px; font-family: "Barlow Condensed", sans-serif; font-weight: 700; font-size: 37px; color: var(--sky); letter-spacing: 0.5px; }
  .contact { position: absolute; left: 480px; top: 110px; font-size: 17.5px; line-height: 22px; }
  .contact-row { display: flex; }
  .contact-label { font-weight: 700; width: 71px; }

  /* Photo band */
  .photo-band { position: absolute; left: 0; top: 217px; width: 849px; height: 515px; }
  .photo-main { position: absolute; left: 0; top: 0; width: 410px; height: 515px;
    background: linear-gradient(180deg, var(--photo-sky) 0%, #8fb8e6 30%, var(--photo-tan) 55%, #c7a37c 100%); }
  .photo-shade { position: absolute; left: 410px; top: 0; width: 439px; height: 515px;
    background: linear-gradient(180deg, var(--photo-dark) 0%, #323842 45%, var(--photo-dark-low) 100%); }
  .headline { position: absolute; left: 480px; top: 42px; font-family: "Barlow Condensed", sans-serif; font-weight: 700; font-size: 53px; line-height: 61.5px; color: var(--white); }

  /* Info section */
  .info { position: absolute; left: 0; top: 732px; width: 849px; height: 369px; background: var(--brand-blue); }
  .column { position: absolute; top: 28px; }
  .column--services { left: 52px; width: 340px; }
  .column--about { left: 450px; width: 372px; }
  .column-title { display: flex; align-items: center; gap: 24px; font-family: "Barlow Condensed", sans-serif; font-weight: 700; font-size: 29px; letter-spacing: 0.3px; height: 32px; }
  .column-title::before { content: ""; width: 5px; height: 20px; background: var(--white); }
  .list { list-style: none; margin-top: 20px; }
  .list li { position: relative; padding-left: 31px; font-size: 15.5px; line-height: 19.5px; }
  .list li::before { content: ""; position: absolute; left: 0; top: 5px; width: 11px; height: 11px; border: 2px solid var(--bullet); border-radius: 50%; }
  .list--services li { margin-bottom: 21.5px; }
  .list--about li { margin-bottom: 16px; }

  /* Footer */
  .footer { position: absolute; left: 0; top: 1101px; width: 849px; height: 99px; background: var(--ink); text-align: center; }
  .cta-title { margin-top: 18px; font-family: "Barlow Semi Condensed", sans-serif; font-weight: 700; font-size: 28px; line-height: 30px; color: var(--sky); }
  .cta-text { font-size: 16.8px; line-height: 21px; color: var(--white); }
</style>
</head>
<body>
<main class="flyer">
  <header class="header">
    <div class="brand">
      <span class="brand-mark"></span>
      <span class="brand-name">Corvane Property Solutions, LLC</span>
    </div>
    <div class="license">ROC #318502</div>
    <div class="contact">
      <div class="contact-row"><span class="contact-label">Phone:</span><span>(602) 555-0147</span></div>
      <div class="contact-row"><span class="contact-label">Email:</span><span>solutions@corvaneproperties.com</span></div>
      <div class="contact-row"><span class="contact-label">Website:</span><span>www.corvanepropertysolutions.com</span></div>
    </div>
  </header>

  <section class="photo-band">
    <div class="photo-main" role="img" aria-label="Photo of a tile-roofed home with a paved patio under a blue sky"></div>
    <div class="photo-shade" role="img" aria-label="Darkened photo of a backyard pool and patio"></div>
    <h1 class="headline">Top Quality<br>Drywall Repair,<br>Installation,<br>Painting &amp;<br>Insurance<br>Restoration<br>Services!</h1>
  </section>

  <section class="info">
    <div class="column column--services">
      <h2 class="column-title">SERVICES</h2>
      <ul class="list list--services">
        <li>Drywall Repair and Hole Patching</li>
        <li>New Drywall Installation and Hanging</li>
        <li>Popcorn Ceiling Removal</li>
        <li>All Textures- Orange Peel, Knockdown,</li>
        <li>Smooth Finish, Skip Trowel</li>
        <li>Complete Interior and Exterior Painting</li>
        <li>Insurance Restoration- Fire, Water Damage</li>
      </ul>
    </div>
    <div class="column column--about">
      <h2 class="column-title">ABOUT US</h2>
      <ul class="list list--about">
        <li>Corvane Property Solutions LLC has 10+ years' experience here in Maricopa County.</li>
        <li>Locally owned family business with an A+ TRB rating, full general contractor license/insurance.</li>
        <li>We can handle your entire drywall, painting, or restoration project- no need to hire multiple companies or subs. Just bring us in and let us give you a stress free one stop shop experience.</li>
        <li>Customers who work with us typically hire us for our professional quality work that's always consistent, reliable, and completed on deadline.</li>
      </ul>
    </div>
  </section>

  <footer class="footer">
    <p class="cta-title">Call To Action To Incorporate:</p>
    <p class="cta-text">Contact us today to discuss your project and receive a free estimate within 72 hours!</p>
  </footer>
</main>
</body>
</html>
```